International wholesale business needs a business card

We need a business card.

Company Details:
Company Name and logo
Address, Phone number, Website
Employee Details:
Name, Designation, Mobile Number & Email address

Logo file is attached.

```html
<!DOCTYPE html>
<html lang="en">
<head>
<meta charset="utf-8">
<title>Norvale Trading – Business Card</title>
<link href="https://fonts.googleapis.com/css2?family=Open+Sans:wght@400;600;700&display=swap" rel="stylesheet">
<style>
  :root {
    --backdrop: #3a3a3a;
    --card: #141414;
    --accent: #d4262b;
    --text: #f2f2f2;
    --muted: #8a8a8a;
    --gloss: #2c2c2c;
  }
  * { box-sizing: border-box; margin: 0; padding: 0; }
  html, body {
    width: 1200px; height: 801px; overflow: hidden;
    background: var(--backdrop);
    font-family: "Open Sans", Arial, sans-serif;
  }
  .sheet {
    position: relative; width: 1200px; height: 801px;
    display: flex; align-items: center; justify-content: center; gap: 40px;
  }
  .card {
    position: relative; width: 520px; height: 297px;
    background: var(--card);
    border: 2px solid var(--accent);
  }
  /* front */
  .brand {
    position: absolute; left: 22px; top: 0; bottom: 0; width: 210px;
    display: flex; align-items: center; gap: 9px;
  }
  .brand-square {
    width: 12px; height: 12px; background: var(--accent); flex: none;
  }
  .brand-name {
    color: var(--accent); font-weight: 600; font-size: 16px;
    letter-spacing: 0.5px; white-space: nowrap; text-transform: uppercase;
  }
  .divider {
    position: absolute; left: 240px; top: 0; bottom: 0;
    width: 1px; background: var(--accent);
  }
  .details {
    position: absolute; left: 262px; top: 46px; right: 20px;
    color: var(--text); font-size: 13px; line-height: 1.45;
  }
  .person-name {
    color: var(--accent); font-weight: 700; font-size: 18px;
    text-transform: uppercase; line-height: 1.2;
  }
  .person-role { color: var(--muted); font-size: 13px; margin-bottom: 14px; }
  .address { margin-bottom: 14px; }
  .contact-list { list-style: none; }
  .contact-list li { display: flex; align-items: center; gap: 8px; }
  .contact-list svg { width: 11px; height: 11px; flex: none; }
  /* back */
  .back { display: flex; align-items: center; justify-content: center; }
  .back-name {
    color: var(--gloss); font-weight: 600; font-size: 22px;
    letter-spacing: 1px; text-transform: uppercase;
  }
</style>
</head>
<body>
<main class="sheet">
  <section class="card front" aria-label="Card front">
    <div class="brand">
      <span class="brand-square"></span>
      <span class="brand-name">Norvale Trading</span>
    </div>
    <div class="divider"></div>
    <div class="details">
      <p class="person-name">Daniel Reyes</p>
      <p class="person-role">President</p>
      <p class="address">1840 Harbor View Lane<br>Seacliff CA 92100</p>
      <ul class="contact-list">
        <li>
          <svg viewBox="0 0 12 12" aria-hidden="true"><path fill="var(--accent)" d="M2.5 1l2 2.2-1 1.3a6 6 0 0 0 4 4l1.3-1 2.2 2-1.2 1.5C5 11 1 7 1 2.2z"/></svg>
          555-210-4870
        </li>
        <li>
          <svg viewBox="0 0 12 12" aria-hidden="true"><rect x="3" y="1" width="6" height="10" rx="1" fill="none" stroke="var(--accent)" stroke-width="1.3"/></svg>
          555-210-4870
        </li>
        <li>
          <svg viewBox="0 0 12 12" aria-hidden="true"><rect x="1" y="2.5" width="10" height="7" fill="var(--accent)"/><path d="M1 2.5l5 4 5-4" fill="none" stroke="var(--card)" stroke-width="1"/></svg>
          daniel@norvaletrading.com
        </li>
        <li>
          <svg viewBox="0 0 12 12" aria-hidden="true"><circle cx="6" cy="6" r="5" fill="var(--accent)"/><path d="M1 6h10M6 1c-2.5 3-2.5 7 0 10M6 1c2.5 3 2.5 7 0 10" fill="none" stroke="var(--card)" stroke-width=".8"/></svg>
          www.norvaletrading.com
        </li>
      </ul>
    </div>
  </section>
  <section class="card back" aria-label="Card back">
    <span class="back-name">Norvale Trading</span>
  </section>
</main>
</body>
</html>
```